Golf Brochure + Business Card Design Project – Larchmere Wellness.

Task Description

We are looking for a premium tri-fold brochure (8.5x11 letter, folded) plus a new business card design for Larchmere Wellness. Both need to look polished, elegant, and professional — something that would feel at home in a golf club environment.

Brochure Scope:
• Tri-fold brochure promoting our new golf-specific services
• Incorporate brand colors: deep hunter green, cream, and gold accents
• Clean, modern typography (professional, not playful)
• Layout will follow the copy provided (final copy attached, no rewriting needed)
• Imagery: mature golfers (50+), golf lifestyle shots, no generic stocky images
• Include QR code placement linking to booking page
• Deliverables: print-ready PDF with bleed/crop (CMYK), high-res PDF (digital), and source file (InDesign or Illustrator)

Business Card Scope:
• Front + back design
• Consistent with brand colors and fonts
• Space for name, title, phone, email, and website
• Deliverables: print-ready PDF with bleed/crop (CMYK) + source file (AI or InDesign)
• If possible, provide editable template for future staff cards

Timeline:
• First draft within 5–7 days
• 2 rounds of revisions included

Budget:
$300 USD (total for both brochure + business card)

I’ll provide finalized copy if you accept the project.
Project description (paste this whole block in that box)

We need a premium tri-fold brochure (8.5”×11” letter, folded) and a new business card design for Larchmere Wellness. This will be presented to golf course managers and members, so the look must be elegant, restrained, and country-club-classy.

Scope — Brochure
• Format: Tri-fold, 8.5”×11”. Please set 0.125” bleed on all sides and keep critical text ≥0.125–0.25” inside the trim.
• Purpose: Promote Larchmere Wellness’ golf-specific services for adults 50+.
• Copy: We will provide finalized copy in a Word doc after acceptance. No rewriting needed — please focus on layout and polish.
• Imagery (required):
• Golf-first images (ball on tee/green, mature golfers mid-swing, and golf course landscapes at golden hour).
• 1–2 real Larchmere Wellness gym photos on inside panels (trainer with client doing golf-relevant movement: stretch, rotation, balance).
• Visual style: Premium, quiet, lots of white/negative space, balanced grids; no clutter.
• Brand colors (required): Hunter Green #0C2E1F, Gold #CBA135, Cream #F5F2EB. Convert for CMYK print while preserving the look.
• Typography: Clean, legible serif + sans pairing (e.g., modern serif for headlines, humanist/neo-grotesk sans for body). You may propose suitable professional fonts; avoid playful/novelty fonts.
• Elements to include:
• Our logo (we will upload).
• QR code placement to booking page (we will supply the URL / QR asset).
• Simple icon treatment for the three complimentary options (Strength & Mobility, Stretch Therapy, Corelyn + Assessment).
• Deliverables:
• Print-ready PDF (CMYK, with bleed & crop marks, PDF/X-1a or PDF/X-4)
• High-res digital PDF (no bleed)
• Source file (InDesign or Illustrator) + packaged fonts/links or outlined type as appropriate.

Scope — Business Card
• Size: 3.5”×2” (US standard) with 0.125” bleed; keep text ≥0.125” from trim.
• Front/back design; consistent with brochure branding.
• Fields: Name, Title, Phone, Email, Website, Address; optional small QR on back.
• Deliverables: Print-ready PDF (CMYK, bleed & crops) + Source file (AI/INDD). Provide an editable template for staff names.

Process & Timing
• Initial concept for brochure + card within 5–7 days of acceptance.
• 2 rounds of revisions included.
• Please start with a clean layout concept using placeholder images/text blocks; we’ll drop in final copy/assets immediately after acceptance.

Stock & Licensing
• You may propose stock images that fit the brief (we’re fine approving Pictavault or equivalent). Please note any license fees separately if needed.

Usage Rights
• We require full usage rights to the final designs for print & digital.

Target Market(s)

Golfers 50+ in Victoria, BC: quality-oriented, health-conscious, want to play longer, stronger, and pain-free. Country-club aesthetic; expect polished, professional materials.

Industry/Entity Type

Health & Fitness — Golf Performance / Longevity Studio

Font styles to use
Serif
Sans Serif

Requirements
Must have
• • Golf-first imagery + 1–2 real Larchmere Wellness photos inside. • Brand colors: #0C2E1F (Hunter Green), #CBA135 (Gold), #F5F2EB (Cream). • Premium, restrained layout; ample negative space; no clutter. • Clean professional serif + sans type pairing; highly legible. • Space for logo and QR code (booking). • Correct print specs (bleed, crops, CMYK). • Deliverables: print-ready PDFs (brochure + card), digital PDF, source files.
Nice to have
• • Subtle texture or grain in backgrounds (very light) to add sophistication. • A second brochure cover variation (ball on tee vs. course landscape) at concept stage.
Should not have
• • Cheesy/posed “stocky” groups; overly young models; beer/alcohol imagery. • Over-saturated greens/blues; gimmicky gradients or clip art. • Generic fitness/bodybuilding shots unrelated to golf performance.

```html
<!DOCTYPE html>
<html lang="en">
<head>
<meta charset="utf-8">
<title>Larchmere Wellness – Golf Brochure and Business Card</title>
<link rel="stylesheet" href="https://fonts.googleapis.com/css2?family=Montserrat:wght@500;600&family=Roboto:wght@400;700&display=swap">
<style>
  :root {
    --board: #d9d9db;
    --hunter: #0f3a36;
    --hunter-deep: #0c2e2b;
    --white: #ffffff;
    --ink: #1c1c1c;
    --soft: #d7e2df;
    --shadow: 0 6px 10px rgba(0,0,0,0.35);
  }
  * { box-sizing: border-box; margin: 0; padding: 0; }
  html, body { width: 749px; height: 1200px; overflow: hidden; background: var(--board); }
  body { position: relative; font-family: "Roboto", Arial, sans-serif; color: var(--ink); }

  .piece { position: absolute; background: var(--white); box-shadow: var(--shadow); overflow: hidden; }
  .wordmark { font-family: "Montserrat", Arial, sans-serif; font-weight: 600; color: var(--hunter); letter-spacing: 0.06em; line-height: 1.2; display: flex; align-items: center; gap: 5px; white-space: nowrap; }
  .wordmark .dot { width: 7px; height: 7px; border-radius: 50%; background: var(--hunter); flex: none; }

  /* Business card front */
  .card-front { left: 48px; top: 52px; width: 313px; height: 191px; }
  .card-wave { position: absolute; left: 0; top: 0; }
  .card-front .wordmark { position: absolute; right: 16px; top: 44px; font-size: 9px; }
  .card-name { position: absolute; left: 24px; top: 101px; color: var(--white); font-family: "Montserrat", Arial, sans-serif; font-weight: 600; font-size: 12px; }
  .card-title { position: absolute; left: 24px; top: 118px; color: var(--soft); font-size: 7.5px; }
  .card-contacts { position: absolute; left: 24px; top: 140px; list-style: none; color: var(--white); font-size: 7.5px; }
  .card-contacts li { display: flex; align-items: center; gap: 7px; height: 12.5px; }
  .contact-icon { width: 6px; height: 6px; flex: none; }

  /* Business card back */
  .card-back { left: 388px; top: 52px; width: 313px; height: 191px; }
  .card-back .wordmark { position: absolute; left: 0; right: 0; top: 62px; justify-content: center; font-size: 12px; }
  .card-back-band { position: absolute; left: 0; right: 0; bottom: 0; height: 44px; background: var(--hunter); border-radius: 34px 34px 0 0; display: flex; align-items: center; justify-content: center; }
  .tagline { color: #e6ecea; font-size: 7.5px; letter-spacing: 0.2em; }

  /* Brochure outside */
  .brochure-outside { left: 94px; top: 282px; width: 560px; height: 432px; }
  .photo-trainer { position: absolute; left: 0; top: 0; width: 187px; height: 432px; background: linear-gradient(160deg, #1a1d20 0%, #3b2a1e 40%, #7a4a2a 55%, #1e2024 80%, #141517 100%); }
  .outside-intro { position: absolute; left: 208px; top: 25px; width: 150px; font-size: 6.8px; line-height: 1.45; }
  .outside-intro ul { list-style: none; margin-top: 9px; }
  .outside-intro li::before { content: "● "; font-size: 5px; vertical-align: 1px; }
  .outside-credentials { position: absolute; left: 208px; top: 110px; width: 150px; text-align: center; font-size: 6.8px; line-height: 1.45; }
  .brochure-outside .logo-spot { position: absolute; left: 400px; top: 58px; font-size: 11px; }
  .golf-scene { position: absolute; inset: 0; }
  .outside-contacts { position: absolute; left: 195px; top: 290px; width: 170px; text-align: center; color: var(--white); font-weight: 700; font-size: 9.5px; line-height: 1.45; }
  .headline { position: absolute; right: 16px; top: 224px; text-align: right; color: var(--white); font-family: "Roboto", Arial, sans-serif; font-weight: 700; line-height: 1.1; }
  .headline .big { display: block; font-size: 27px; }
  .headline .sub { display: block; font-size: 14px; margin-top: 3px; }
  .exclusive-note { position: absolute; left: 210px; top: 390px; width: 140px; text-align: center; color: var(--white); font-weight: 700; font-size: 9px; line-height: 1.45; }
  .invite-note { position: absolute; right: 16px; top: 388px; width: 180px; text-align: right; color: var(--white); font-size: 9px; line-height: 1.45; }

  /* Brochure inside */
  .brochure-inside { left: 94px; top: 739px; width: 560px; height: 432px; background: var(--hunter-deep); }
  .inside-scene { position: absolute; left: 0; top: 0; }
  .inside-col { position: absolute; color: var(--white); font-size: 6.8px; line-height: 1.5; }
  .inside-lead { left: 13px; top: 38px; width: 170px; }
  .inside-benefits { left: 13px; top: 196px; width: 165px; }
  .inside-benefits ul { list-style: none; margin-top: 8px; padding-left: 12px; }
  .inside-benefits li { position: relative; padding-left: 8px; margin-bottom: 9px; }
  .inside-benefits li::before { content: ""; position: absolute; left: -2px; top: 3px; width: 3px; height: 3px; border-radius: 50%; background: var(--white); }
  .inside-closing { left: 13px; top: 384px; width: 165px; }
  .offer-panel { left: 383px; top: 30px; width: 165px; }
  .offer-panel h3 { font-size: 6.8px; font-weight: 400; margin-top: 40px; }
  .offer-panel ul { list-style: none; margin-top: 12px; padding-left: 10px; }
  .offer-panel li { position: relative; padding-left: 10px; margin-bottom: 11px; }
  .offer-panel li::before { content: ""; position: absolute; left: 0; top: 3px; width: 3px; height: 3px; border-radius: 50%; background: var(--white); }
  .offer-value { left: 383px; top: 351px; width: 170px; }
  .offer-redeem { left: 383px; top: 381px; width: 165px; }
</style>
</head>
<body>

<section class="piece card-front" aria-label="Business card front">
  <svg class="card-wave" width="313" height="191" viewBox="0 0 313 191" aria-hidden="true">
    <path d="M0,42 C70,36 115,38 150,70 C185,104 210,116 250,116 L313,116 L313,191 L0,191 Z" fill="#0f3a36"/>
  </svg>
  <div class="wordmark"><span class="dot"></span><span>Larchmere Wellness</span></div>
  <p class="card-name">Maren Ashdown</p>
  <p class="card-title">Owner | Larchmere Wellness</p>
  <ul class="card-contacts">
    <li><svg class="contact-icon" viewBox="0 0 10 10" aria-hidden="true"><path d="M2 0 L4 2.5 L3 4 Q4.5 6 6 7 L7.5 6 L10 8 L8.5 10 Q3 9 0 1.5 Z" fill="#d7e2df"/></svg>250-555-0147</li>
    <li><svg class="contact-icon" viewBox="0 0 10 10" aria-hidden="true"><rect x="0.5" y="2" width="9" height="6.5" fill="#d7e2df"/><path d="M0.5 2 L5 5.5 L9.5 2" fill="none" stroke="#0f3a36" stroke-width="1"/></svg>maren@larchmerewellness.biz</li>
    <li><svg class="contact-icon" viewBox="0 0 10 10" aria-hidden="true"><circle cx="5" cy="5" r="4.3" fill="none" stroke="#d7e2df" stroke-width="1.2"/><path d="M0.7 5 H9.3 M5 0.7 Q2.5 5 5 9.3 M5 0.7 Q7.5 5 5 9.3" fill="none" stroke="#d7e2df" stroke-width="0.9"/></svg>larchmerewellnessvictoria.com</li>
  </ul>
</section>

<section class="piece card-back" aria-label="Business card back">
  <div class="wordmark"><span class="dot"></span><span>Larchmere Wellness</span></div>
  <div class="card-back-band"><p class="tagline">Strength · Mobility · Longevity</p></div>
</section>

<section class="piece brochure-outside" aria-label="Brochure outside panels">
  <div class="photo-trainer" role="img" aria-label="Photo of a trainer stretching with a resistance band in a dark studio"></div>
  <div class="outside-intro">
    <p>Located in Victoria, Larchmere Wellness is a private training studio specializing in:</p>
    <ul>
      <li>Personal Training for adults 40+</li>
      <li>Golf-specific performance coaching</li>
      <li>Stretch therapy and athletic therapy</li>
      <li>Longevity &amp; strength training</li>
    </ul>
  </div>
  <p class="outside-credentials">Every coach holds a degree in Sports Science — ensuring safe, proven, results-driven programs.</p>
  <div class="wordmark logo-spot"><span class="dot"></span><span>Larchmere Wellness</span></div>
  <svg class="golf-scene" width="560" height="432" viewBox="0 0 560 432" role="img" aria-label="Photo of a golf ball on a tee in the grass beside a driver">
    <defs>
      <linearGradient id="turf" x1="0" y1="0" x2="0" y2="1">
        <stop offset="0" stop-color="#1f4f1c"/>
        <stop offset="0.55" stop-color="#3f7a2a"/>
        <stop offset="1" stop-color="#2c6320"/>
      </linearGradient>
    </defs>
    <path d="M187,432 L187,225 C225,175 290,180 370,182 C450,184 515,170 560,150 L560,432 Z" fill="url(#turf)"/>
  </svg>
  <p class="outside-contacts">250-555-0147<br>maren@larchmerewellness.biz<br>larchmerewellnessvictoria.com</p>
  <h1 class="headline"><span class="big">Stronger.</span><span class="big">Smoother.</span><span class="sub">Longer off the Tee.</span></h1>
  <p class="exclusive-note">This invitation is exclusive and non-transferable.</p>
  <p class="invite-note">An exclusive invitation for select members of Larchmere Wellness.</p>
</section>

<section class="piece brochure-inside" aria-label="Brochure inside panels">
  <svg class="inside-scene" width="560" height="432" viewBox="0 0 560 432">
    <defs>
      <linearGradient id="gym" x1="0" y1="0" x2="1" y2="0">
        <stop offset="0" stop-color="#1c2a2a"/>
        <stop offset="0.5" stop-color="#2e2e30"/>
        <stop offset="1" stop-color="#3a3a3e"/>
      </linearGradient>
    </defs>
    <polygon points="0,189 373,4 373,432 0,432" fill="url(#gym)" role="img" aria-label="Photo of a mature golfer doing a rotational cable exercise in the studio"/>
    <polygon points="0,189 187,96 187,432 0,432" fill="#0c2e2b" opacity="0.55"/>
    <polygon points="373,2 118,141 141,154" fill="#ffffff"/>
  </svg>
  <p class="inside-col inside-lead">The game changes as we age. Distance fades, flexibility tightens, and recovery after 18 holes takes longer than it used to. But that doesn't mean your best golf is behind you.</p>
  <div class="inside-col inside-benefits">
    <p>At Larchmere Wellness, we specialize in helping golfers 50+ build the strength, mobility, and balance needed to:</p>
    <ul>
      <li>Add yards off the tee with rotational strength training</li>
      <li>Maintain a fluid swing with improved shoulder and hip mobility</li>
      <li>Reduce back and joint pain with targeted stability work</li>
      <li>Walk off the 18th green feeling strong, not sore</li>
    </ul>
  </div>
  <p class="inside-col inside-closing">This isn't generic gym training — it's science-based coaching tailored to golfers.</p>
  <div class="inside-col offer-panel">
    <p>As one of the club's most valued golfers, you've been hand-selected to receive a complimentary premium experience at Larchmere Wellness.</p>
    <h3>Choose one golf-specific session:</h3>
    <ul>
      <li>Golf Strength &amp; Mobility Session Add rotational power for more distance and protect your back.</li>
      <li>Golf Flexibility &amp; Stretch Therapy Unlock tighter hips &amp; shoulders to swing easier and play longer.</li>
      <li>Corelyn Scan + Golf Wellness Assessment Identify muscle imbalances and posture issues holding your game back.</li>
      <li>Golf-Specific Personal Training Session One-on-one workout to boost club-head speed, balance, and confidence.</li>
    </ul>
  </div>
  <p class="inside-col offer-value">Valued at $110–$125 | Reserved exclusively for select golf members</p>
  <p class="inside-col offer-redeem">To redeem: Contact Larchmere Wellness directly. This invitation is limited and not available to the public.</p>
</section>

</body>
</html>
```